Zielgruppe
Wir sind ein kleiner familiengeführter Weinbaubetrieb am Wagram und suchen einen modernen und naturnahen Namen und ein Etikett mit Blickfang für unseren Wermut, aus handgepflückten regionalen Wildkräutern mit Rosewein vom Zweigelt. Charakeristik des Getränks: Aperitif, Zitrusnote, leichte Bitternote, mit Tonic water als Cocktail.
Unsere Zielgruppe: kaufkräftige Genussmenschen im mittleren Alter
Aufgabenstellung
Etikett für 0,5l Flasche, Flasche noch nicht festgelegt, Etikettenhöhe: 65mm
Was soll draufstehen: Name, Vermouth, local botanicals, handcrafted, small batch

```html
<!DOCTYPE html>
<html lang="en">
<head>
<meta charset="utf-8">
<title>Feldrosa Vermouth – Label</title>
<link rel="stylesheet" href="https://fonts.googleapis.com/css2?family=Mrs+Saint+Delafield&family=Space+Mono&display=swap">
<style>
  :root {
    --page: #ffffff;
    --label-base: #eaf3f0;
    --label-vein: #dbece6;
    --panel: #fbfdfc;
    --frame: #a9cfc3;
    --ink: #1f3a4f;
    --mint: #a8d5c2;
    --script: #9ccbb8;
  }
  * { margin: 0; padding: 0; box-sizing: border-box; }
  html, body {
    width: 807px;
    height: 1200px;
    overflow: hidden;
    background: var(--page);
  }
  .canvas {
    position: relative;
    width: 807px;
    height: 1200px;
  }
  .label {
    position: absolute;
    left: 23px;
    top: 54px;
    width: 760px;
    height: 1092px;
  }
  .label-texture {
    position: absolute;
    inset: 0;
    background:
      radial-gradient(ellipse at 20% 15%, var(--label-vein) 0%, transparent 55%),
      radial-gradient(ellipse at 85% 80%, var(--label-vein) 0%, transparent 50%),
      var(--label-base);
  }
  .panel {
    position: absolute;
    left: 92px;
    top: 197px;
    width: 582px;
    height: 749px;
    background: var(--panel);
    border: 3px solid var(--frame);
  }
  .product-name {
    position: absolute;
    top: 40px;
    left: 0;
    right: 0;
    text-align: center;
    font-family: "Space Mono", monospace;
    font-weight: 400;
    font-size: 36px;
    color: var(--ink);
    letter-spacing: 1px;
  }
  .brand-mark {
    position: absolute;
    top: 155px;
    left: 0;
    right: 0;
    display: flex;
    align-items: center;
    justify-content: center;
    gap: 18px;
  }
  .brand-dot {
    width: 100px;
    height: 100px;
    border-radius: 50%;
    background: var(--mint);
  }
  .brand-name {
    font-family: "Space Mono", monospace;
    font-weight: 400;
    font-size: 30px;
    color: var(--mint);
  }
  .script-title {
    position: absolute;
    top: 320px;
    left: 100px;
    width: 380px;
    height: 230px;
    font-family: "Mrs Saint Delafield", cursive;
    font-weight: 400;
    color: var(--script);
  }
  .script-title span {
    position: absolute;
    white-space: nowrap;
    line-height: 1;
  }
  .script-first {
    left: 70px;
    top: 0;
    font-size: 110px;
  }
  .script-second {
    left: 10px;
    top: 95px;
    font-size: 120px;
  }
  .descriptor {
    position: absolute;
    top: 590px;
    left: 0;
    right: 0;
    text-align: center;
    font-family: "Space Mono", monospace;
    font-weight: 400;
    font-size: 31px;
    line-height: 39px;
    color: var(--ink);
  }
</style>
</head>
<body>
  <main class="canvas">
    <section class="label">
      <div class="label-texture" role="img" aria-label="Soft mint marbled paper texture"></div>
      <div class="panel">
        <h1 class="product-name">Feldrosa Vermouth</h1>
        <div class="brand-mark">
          <span class="brand-dot"></span>
          <span class="brand-name">Feldrosa</span>
        </div>
        <h2 class="script-title">
          <span class="script-first">Rose</span>
          <span class="script-second">Vermouth</span>
        </h2>
        <p class="descriptor">Handcrafted Small Batch<br>Vermouth with Rose Wine &amp;<br>local Botanicals</p>
      </div>
    </section>
  </main>
</body>
</html>
```